Construction company featuring multiple photos to highlight work. Looking for clean modern design.

-Clean and modern design ****(SEE THUMBNAIL FILES FOR EASY PROJECT GROUPINGS)
-Looking for photos to be highlighted in a unique way to show before and after photos of Construction projects. (Please refer to this website for a possible layout . This is NOT our company but we like the layout of photos www.plovanstudio.com We dont want to copy any website but wanted to guide designers in the right direction.
will be uploading more content but looking for photo layout as a big part of the website design
******VERY IMPORTANT. Please see the 5 file uploads called THUMBNAILS for help with photo groups. this is to help you see the groups of photos that need to go together. (I have then uploaded the individual photos separately from thumbnail for better quality photos.)
****The photos that have been uploaded are labeled by room and house number(For example 3106 is a house number then it will say before or progress or after to show the project. . we would prefer to highlight projects by bathroom remodel, kitchen remodel, wood flooring and trim package jobs etc. NOT by house number. the house number was only to organize the photos not to list them on website by house number.
++++ Would like it to be very clear that the before photos are before construction begins.
++++Was maybe picturing small icons to show the before photos and a Larger slideshow showing the completed designs.
++++Feature photos would be the 3106 photos Kitchen/family room , bathrooms labeled 3106 is most current work.
++++Some photo catagories could be ....
-Kitchens Photos
-Bathrooms Photos
-Flooring/Doors/Trim Photos
-New Construction/Real Estate Renovations Photos
-Home Additions Photos
-Insurance Claims Fire and Water Damage Photos
-----Our Services:
-Remodeling Kitchen & Bath
-Insurance Claims Fire and Water Damage Repairs
-Home Additions / New Home Construction
-Flooring, tile, decking
-Custom built-ins and trim/door remodel
-Interior & Exterior Painting
-Roofing

Contact Us information:
Ashmoor Construction (Charleston South Carolina)
827 Tarrow Lane
Suite 415
Mount Pleasant, SC 29471
Owner: Dennis Roulard
Phone (803) 555-0147
Email: droulard@ashmoorbuild.com
Ashmoor Construction Website Content
-----Bio: Dennis Roulard, owner of Ashmoor Construction has over 17 years of experience working with customers on remodeling, renovation projects, and insurance related fire and water damage repairs.
----Contact us today to set up a free consultation.
(803) 555-0147
Will upload more text content soon

Industry/Entity Type

Residential General Contractor

Coding

Coded - Design and coding required

Requirements
Must have
• Ashmoor Construction Website Content Bio: Dennis Roulard, owner of Ashmoor Construction has over 17 years of experience working with customers on remodeling, renovation projects, and insurance related fire and water damage repairs. Contact us today to set up a free consultation. (803) 555-0147
Nice to have
• Nice to have a contact us page that can have a call now button with phone number or email. Would be really great if there could a way to have reviews populate from Verlo reviews.

```html
<!DOCTYPE html>
<html lang="en">
<head>
<meta charset="utf-8">
<title>Ashmoor Construction</title>
<link href="https://fonts.googleapis.com/css2?family=Jost:ital,wght@0,300;0,400;0,500;0,600;0,700;1,400&display=swap" rel="stylesheet">
<style>
:root{
  --blue:#1565ab;
  --link:#3a86c8;
  --ink:#2b2b2b;
  --dark:#3a3a3a;
  --cream:#f7f3ef;
  --black:#050505;
  --white:#fff;
}
*{margin:0;padding:0;box-sizing:border-box}
html,body{width:1200px;height:4276px;overflow:hidden}
body{font-family:'Jost',sans-serif;color:var(--ink);background:var(--white);position:relative}
.abs{position:absolute}
.img{position:absolute}
/* hero */
.hero-panel{left:0;top:0;width:443px;height:642px;background:var(--blue)}
.hero-photo{left:443px;top:0;width:757px;height:642px;
  background:
    radial-gradient(ellipse 38% 42% at 52% 48%,rgba(250,250,246,.95) 0%,rgba(242,241,235,.7) 45%,rgba(242,241,235,0) 100%),
    radial-gradient(ellipse 30% 30% at 80% 72%,rgba(190,120,100,.55),rgba(190,120,100,0)),
    linear-gradient(90deg,rgba(120,130,80,.55) 0%,rgba(120,130,80,0) 22%,rgba(120,130,80,0) 80%,rgba(90,110,70,.5) 100%),
    linear-gradient(180deg,#c9d9e6 0%,#dfe6e4 25%,#ece9df 55%,#9aa67a 82%,#556b3a 100%)}
.logo{left:100px;top:30px;width:175px;text-align:center;color:var(--white);font-weight:700;font-size:30px;letter-spacing:2px;line-height:1}
.logo small{display:block;font-size:11px;font-weight:500;letter-spacing:3px;margin-top:6px}
.nav{left:457px;top:28px;display:flex;gap:21px;font-size:15px;font-weight:500;text-transform:uppercase}
.nav a{color:var(--ink);text-decoration:none}
.nav a.active{color:var(--link)}
.nav-phone{left:938px;top:12px;width:162px;height:50px;background:var(--dark);color:var(--white);font-size:15px;font-weight:500;display:flex;align-items:center;justify-content:center;gap:6px}
.hero-kicker{left:100px;top:195px;color:var(--white);font-style:italic;font-size:17.5px}
.hero-years{left:104px;top:222px;color:var(--white);font-weight:700;font-size:68px;line-height:1}
.hero-exp{left:100px;top:296px;color:var(--white);font-weight:600;font-size:30px;letter-spacing:8px;line-height:1.1}
.hero-inset{left:98px;top:349px;width:384px;height:382px;background:var(--white);padding:10px;box-shadow:0 4px 18px rgba(0,0,0,.18)}
.hero-inset div{width:100%;height:100%;
  background:
    radial-gradient(ellipse 45% 40% at 38% 45%,rgba(222,186,172,.95),rgba(222,186,172,0)),
    radial-gradient(ellipse 30% 25% at 55% 80%,rgba(150,80,60,.7),rgba(150,80,60,0)),
    linear-gradient(180deg,#7fa466 0%,#cfb3a4 40%,#c49a88 65%,#4c6b35 100%)}
.scroll-arrow{left:592px;top:602px}
/* bio */
.bio-label{left:98px;top:912px;font-size:16px;font-weight:700;letter-spacing:2px;border-bottom:2px solid var(--ink);line-height:1.1}
.bio-name{left:96px;top:938px;font-size:42px;font-weight:300;letter-spacing:.5px;line-height:1.2}
.bio-text{left:100px;top:1007px;width:385px;font-style:italic;font-size:18px;line-height:30px}
.bio-cta{left:100px;top:1166px;font-size:17px;font-weight:600}
.bio-phone{left:98px;top:1196px;font-size:25px;font-weight:500;display:flex;align-items:center;gap:10px}
.bio-photo{left:522px;top:850px;width:578px;height:465px;
  background:
    radial-gradient(ellipse 30% 45% at 35% 60%,rgba(70,70,70,.8),rgba(70,70,70,0)),
    radial-gradient(ellipse 25% 40% at 80% 65%,rgba(60,60,60,.7),rgba(60,60,60,0)),
    radial-gradient(ellipse 25% 30% at 55% 25%,rgba(200,200,200,.7),rgba(200,200,200,0)),
    linear-gradient(180deg,#8d8d8d 0%,#a9a9a9 35%,#6a6a6a 100%)}
/* services */
.services{left:0;top:1422px;width:1200px;height:643px;background:var(--cream)}
.section-title{font-weight:600;font-size:52px;letter-spacing:1px;line-height:1.2}
.services .section-title{left:0;width:1200px;text-align:center;top:72px}
.service{top:168px;width:310px;text-align:center}
.service-icon{height:90px;display:flex;justify-content:center;align-items:center}
.service h3{font-weight:500;font-size:18px;line-height:27px;margin-top:20px;text-transform:uppercase}
.service p{font-size:17px;line-height:26px;margin-top:8px}
.read-more{position:absolute;text-align:center}
.read-more span{font-weight:600;font-size:15px;border-bottom:2px solid var(--link);padding-bottom:2px}
.btn-dark{left:495px;top:508px;width:210px;height:50px;background:var(--dark);color:var(--white);font-weight:600;font-size:16px;display:flex;align-items:center;justify-content:center;letter-spacing:.5px}
/* projects */
.projects-title{left:98px;top:2168px}
.btn-outline{left:892px;top:2175px;width:211px;height:52px;border:2px solid var(--dark);font-weight:500;font-size:15px;display:flex;align-items:center;justify-content:center}
.tabs{left:100px;top:2262px;width:820px;display:flex;flex-wrap:wrap;column-gap:40px;row-gap:18px;font-size:17px}
.tabs span.active{border-bottom:2px solid var(--link)}
.pair{width:492px;height:351px;display:flex}
.pair > div{flex:1;position:relative}
.pair span{position:absolute;bottom:14px;left:16px;color:var(--white);font-weight:600;font-size:18px;text-shadow:0 1px 3px rgba(0,0,0,.5)}
/* contact */
.contact{left:0;top:3250px;width:1200px;height:645px;background:var(--cream)}
.contact .section-title{left:98px;top:112px}
.contact-info{left:98px;top:193px;font-size:17px;line-height:27px}
.contact-info .co{color:var(--link)}
.contact-info .muted{color:#666}
.owner-label{left:98px;top:314px;font-weight:600;font-size:20px}
.owner-name{left:98px;top:348px;font-size:26px;font-weight:300}
.contact-line{left:98px;font-size:17px;display:flex;align-items:center;gap:12px}
.contact-photo{left:578px;top:109px;width:522px;height:429px;
  background:
    radial-gradient(ellipse 22% 22% at 28% 58%,rgba(40,60,110,.55),rgba(40,60,110,0)),
    radial-gradient(ellipse 15% 35% at 90% 55%,rgba(110,80,55,.55),rgba(110,80,55,0)),
    radial-gradient(ellipse 40% 25% at 50% 45%,rgba(160,190,170,.45),rgba(160,190,170,0)),
    linear-gradient(180deg,#e6ecef 0%,#f1f1ee 40%,#d9d6d0 70%,#c3beb4 100%)}
/* footer */
.footer{left:0;top:3893px;width:1200px;height:383px;background:var(--black);color:var(--white)}
.footer .logo{left:512px;top:30px}
.socials{left:140px;top:202px;display:flex;gap:38px}
.socials i{display:block;width:18px;height:18px;border-radius:50%;background:var(--white)}
.vline{top:133px;width:1px;height:182px;background:#666}
.email-label{left:451px;top:148px;font-size:15px}
.email-input{left:451px;top:177px;width:299px;height:43px;border:1px solid var(--white)}
.subscribe{left:451px;top:232px;width:299px;height:42px;border:1px solid var(--white);font-weight:600;font-size:15px;display:flex;align-items:center;justify-content:center;letter-spacing:1px}
.foot-links{left:816px;top:186px;width:284px;text-align:right;font-size:14px;line-height:34px;text-transform:uppercase}
.copyright{left:98px;top:340px;font-size:13px;color:#777}
.copyright b{color:var(--white);font-weight:400}
</style>
</head>
<body>

<header>
  <div class="abs hero-panel"></div>
  <div class="img hero-photo" role="img" aria-label="Large white two-storey home with curved staircase, palms and trees"></div>
  <div class="abs logo">ASHMOOR<small>CONSTRUCTION</small></div>
  <nav class="abs nav">
    <a class="active" href="#">Home</a><a href="#">About Me</a><a href="#">Our Services</a><a href="#">Portfolio</a><a href="#">Contact</a>
  </nav>
  <div class="abs nav-phone">
    <svg width="13" height="13" viewBox="0 0 24 24"><path fill="#fff" d="M6.6 10.8a15 15 0 006.6 6.6l2.2-2.2c.3-.3.7-.4 1-.2 1.1.4 2.3.6 3.6.6.6 0 1 .4 1 1V20c0 .6-.4 1-1 1A17 17 0 013 4c0-.6.4-1 1-1h3.5c.6 0 1 .4 1 1 0 1.3.2 2.5.6 3.6.1.3 0 .7-.2 1z"/></svg>
    (803) 555-0147
  </div>
  <div class="abs hero-kicker">ASHMOOR CONSTRUCTION HAS OVER</div>
  <div class="abs hero-years">17 YEARS</div>
  <div class="abs hero-exp">OF EXPERIENCE</div>
  <div class="abs hero-inset"><div role="img" aria-label="Pink stucco home with curved front staircase among trees"></div></div>
  <svg class="abs scroll-arrow" width="16" height="20" viewBox="0 0 16 20"><path d="M8 0v18M2 12l6 6 6-6" stroke="#fff" stroke-width="1.5" fill="none"/></svg>
</header>

<section class="bio">
  <div class="abs bio-label">BIO</div>
  <h2 class="abs bio-name">DENNIS ROULARD</h2>
  <p class="abs bio-text">Dennis Roulard, owner of Ashmoor Construction has over 17 years of experience working with customers on remodeling, renovation projects, and insurance related fire and water damage repairs.</p>
  <div class="abs bio-cta">Contact us today to set up a free consultation.</div>
  <div class="abs bio-phone">
    <svg width="20" height="20" viewBox="0 0 24 24"><path fill="#3a86c8" d="M6.6 10.8a15 15 0 006.6 6.6l2.2-2.2c.3-.3.7-.4 1-.2 1.1.4 2.3.6 3.6.6.6 0 1 .4 1 1V20c0 .6-.4 1-1 1A17 17 0 013 4c0-.6.4-1 1-1h3.5c.6 0 1 .4 1 1 0 1.3.2 2.5.6 3.6.1.3 0 .7-.2 1z"/></svg>
    (803) 555-0147
  </div>
  <div class="img bio-photo" role="img" aria-label="Black and white family portrait of the owner outdoors by a fountain"></div>
</section>

<section class="abs services">
  <h2 class="abs section-title">OUR SERVICES</h2>
  <div class="abs service" style="left:95px">
    <div class="service-icon" role="img" aria-label="Remodeling house icon"><div style="width:80px;height:80px;border-radius:50%;background:linear-gradient(135deg,#e14a5a,#7b6fd0)"></div></div>
    <h3>Remodeling Kitchen &amp; Bath</h3>
    <p>Phasellus quis justo lectus. Cras tincidunt leo non ornare sollicitudin. Vestibulum auctor vitae orci eget imperdiet.</p>
  </div>
  <div class="abs service" style="left:445px">
    <div class="service-icon" role="img" aria-label="Insurance claim tablet icon"><div style="width:60px;height:80px;border-radius:8px;background:linear-gradient(180deg,#444,#2c2c2c)"></div></div>
    <h3>Insurance Claims Fire and Water Damage Repairs</h3>
    <p>Phasellus quis justo lectus. Cras tincidunt leo non ornare sollicitudin.</p>
  </div>
  <div class="abs service" style="left:790px">
    <div class="service-icon" role="img" aria-label="Room with tiled floor icon"><div style="width:86px;height:86px;background:linear-gradient(180deg,#7d9fc9 0%,#9db7d8 55%,#a45a3c 56%,#7f3f28)"></div></div>
    <h3>Flooring, Tile, Decking</h3>
    <p>Phasellus quis justo lectus. Cras tincidunt leo non ornare sollicitudin. Vestibulum auctor vitae orci eget imperdiet.</p>
  </div>
  <div class="read-more" style="left:95px;width:310px;top:428px"><span>READ MORE</span></div>
  <div class="read-more" style="left:445px;width:310px;top:428px"><span>READ MORE</span></div>
  <div class="read-more" style="left:790px;width:310px;top:428px"><span>READ MORE</span></div>
  <div class="abs btn-dark">VIEW ALL SERVICES</div>
</section>

<section class="projects">
  <h2 class="abs section-title projects-title">RECENT PROJECT</h2>
  <div class="abs btn-outline">VIEW ALL PROJECTS</div>
  <div class="abs tabs">
    <span class="active">Kitchens</span><span>Bathrooms</span><span>Flooring/Doors/Trim</span><span>New Construction/Real Estate Renovations</span><span>Home Additions</span><span>Insurance Claims Fire and Water Damage</span>
  </div>
  <div class="abs pair" style="left:100px;top:2380px">
    <div role="img" aria-label="Laundry room before remodel" style="background:radial-gradient(ellipse 30% 25% at 35% 35%,rgba(255,255,255,.9),rgba(255,255,255,0)),radial-gradient(ellipse 50% 25% at 40% 85%,rgba(120,130,150,.5),rgba(120,130,150,0)),linear-gradient(180deg,#d9dee3,#eef0f1 45%,#a9aeb4)"><span>BEFORE</span></div>
    <div role="img" aria-label="Laundry room after remodel" style="background:radial-gradient(ellipse 30% 35% at 45% 35%,rgba(255,255,255,.95),rgba(255,255,255,0)),radial-gradient(ellipse 40% 20% at 55% 90%,rgba(190,160,120,.6),rgba(190,160,120,0)),linear-gradient(180deg,#e9e7e2,#f5f3ef 50%,#cdbfa8)"><span>AFTER</span></div>
  </div>
  <div class="abs pair" style="left:609px;top:2380px">
    <div role="img" aria-label="Dining room with worn floor before" style="background:radial-gradient(ellipse 30% 20% at 50% 35%,rgba(40,50,80,.7),rgba(40,50,80,0)),radial-gradient(ellipse 60% 30% at 50% 85%,rgba(110,60,35,.85),rgba(110,60,35,0)),linear-gradient(180deg,#e2e0d6,#9d9680 50%,#5a3a26)"><span>BEFORE</span></div>
    <div role="img" aria-label="Finished dining room after" style="background:radial-gradient(ellipse 30% 18% at 50% 20%,rgba(40,40,40,.7),rgba(40,40,40,0)),radial-gradient(ellipse 35% 25% at 50% 70%,rgba(50,50,50,.6),rgba(50,50,50,0)),linear-gradient(180deg,#ecebe7,#f6f5f2 40%,#b89f82)"><span>AFTER</span></div>
  </div>
  <div class="abs pair" style="left:100px;top:2787px">
    <div role="img" aria-label="Kitchen with granite island before" style="background:radial-gradient(ellipse 45% 25% at 60% 60%,rgba(150,110,70,.7),rgba(150,110,70,0)),radial-gradient(ellipse 30% 30% at 75% 85%,rgba(40,50,70,.6),rgba(40,50,70,0)),linear-gradient(180deg,#f4efe4,#e6d9c2 50%,#b8946a)"><span>BEFORE</span></div>
    <div role="img" aria-label="White kitchen with island after" style="background:radial-gradient(ellipse 35% 20% at 55% 65%,rgba(255,255,255,.95),rgba(255,255,255,0)),radial-gradient(ellipse 20% 25% at 15% 45%,rgba(60,60,60,.4),rgba(60,60,60,0)),linear-gradient(180deg,#f2f2f0,#f7f6f3 45%,#c9b49a)"><span>AFTER</span></div>
  </div>
  <div class="abs pair" style="left:609px;top:2787px">
    <div role="img" aria-label="Framing of open kitchen during construction" style="background:radial-gradient(ellipse 40% 40% at 50% 45%,rgba(215,190,140,.8),rgba(215,190,140,0)),radial-gradient(ellipse 50% 25% at 50% 90%,rgba(90,70,55,.7),rgba(90,70,55,0)),linear-gradient(180deg,#b9ac96,#c7ad82 45%,#6f5c4a)"><span>BEFORE</span></div>
    <div role="img" aria-label="Completed white kitchen with pendant lights" style="background:radial-gradient(ellipse 30% 25% at 50% 30%,rgba(170,200,195,.6),rgba(170,200,195,0)),radial-gradient(ellipse 45% 20% at 45% 68%,rgba(255,255,255,.95),rgba(255,255,255,0)),linear-gradient(180deg,#eef0ef,#f6f6f4 45%,#cfcac2)"><span>AFTER</span></div>
  </div>
</section>

<section class="abs contact">
  <h2 class="abs section-title">STAY IN TOUCH</h2>
  <div class="abs contact-info">
    <div><span class="co">Ashmoor Construction</span> <span class="muted">(Charleston South Carolina)</span></div>
    <div>827 Tarrow Lane</div>
    <div>Suite 415</div>
    <div>Mount Pleasant, SC 29471</div>
  </div>
  <div class="abs owner-label">Owner</div>
  <div class="abs owner-name">Dennis Roulard</div>
  <div class="abs contact-line" style="top:400px">
    <svg width="18" height="18" viewBox="0 0 24 24"><path fill="#3a86c8" d="M6.6 10.8a15 15 0 006.6 6.6l2.2-2.2c.3-.3.7-.4 1-.2 1.1.4 2.3.6 3.6.6.6 0 1 .4 1 1V20c0 .6-.4 1-1 1A17 17 0 013 4c0-.6.4-1 1-1h3.5c.6 0 1 .4 1 1 0 1.3.2 2.5.6 3.6.1.3 0 .7-.2 1z"/></svg>
    (803) 555-0147
  </div>
  <div class="abs contact-line" style="top:438px">
    <svg width="18" height="14" viewBox="0 0 24 18"><rect width="24" height="18" rx="2" fill="#3a86c8"/><path d="M1 2l11 8 11-8" stroke="#fff" stroke-width="2" fill="none"/></svg>
    droulard@ashmoorbuild.com
  </div>
  <div class="img contact-photo" role="img" aria-label="Bright home office with desk, cabinets and framed art"></div>
</section>

<footer class="abs footer">
  <div class="abs logo">ASHMOOR<small>CONSTRUCTION</small></div>
  <div class="abs socials" aria-label="Social links"><i></i><i></i><i></i><i></i></div>
  <div class="abs vline" style="left:388px"></div>
  <div class="abs vline" style="left:816px"></div>
  <div class="abs email-label">Enter your email here*</div>
  <div class="abs email-input"></div>
  <div class="abs subscribe">SUBSCRIBE</div>
  <div class="abs foot-links">Home &nbsp;|&nbsp; About Me &nbsp;|&nbsp; Our Services<br>Portfolio &nbsp;|&nbsp; Contact</div>
  <div class="abs copyright">© 2023 <b>Ashmoor Construction</b> All right reserved</div>
</footer>

</body>
</html>
```